Mouthguard Marketing

We specialise in the production of custom made mouthguards for sportsmen and women. These are made by direct public contact or via Dental Surgeons. On our postcard we would need the following...
*Custom made sports guards from £20 (Boxed)
Bleaching trays from £28 (pair) (Boxed)
Orthodontic retainers £28 (pair)
All the above manufactured from advanced pressure and vacuum forming techniques.
Please contact Tom or Gary (01872) 552317 Harlow Dental Laboratory Ltd

Industry/Entity Type

Dental

```html
<!DOCTYPE html>
<html lang="en">
<head>
<meta charset="utf-8">
<title>Guard your mouth – Harlow Dental Laboratory Ltd</title>
<link rel="stylesheet" href="https://fonts.googleapis.com/css2?family=Kalam:wght@700&family=Roboto+Condensed:wght@400;700&family=Roboto:wght@300&display=swap">
<style>
  :root {
    --navy: #2b3290;
    --royal: #1d55a6;
    --red: #c8102e;
    --grey: #555a60;
    --white: #ffffff;
  }
  * { margin: 0; padding: 0; box-sizing: border-box; }
  html, body { width: 1200px; height: 930px; overflow: hidden; background: var(--white); }
  .postcard { position: relative; width: 1200px; height: 930px; overflow: hidden; background: var(--white); font-family: "Roboto Condensed", sans-serif; }

  .sweep { position: absolute; left: 0; top: 0; width: 1200px; height: 930px; }

  .membership { position: absolute; left: 46px; top: 42px; display: flex; align-items: center; height: 150px; }
  .membership__mark { width: 110px; height: 110px; background: var(--royal); }
  .membership__divider { width: 2px; height: 150px; background: var(--royal); margin: 0 18px 0 18px; }
  .membership__text { font-family: "Roboto", sans-serif; font-weight: 300; color: var(--royal); }
  .membership__org { font-size: 23px; line-height: 1; margin-bottom: 16px; }
  .membership__status { font-size: 38px; line-height: 1; }

  .headline { position: absolute; left: 50px; top: 250px; font-family: "Kalam", cursive; font-weight: 700; color: var(--red); font-size: 80px; line-height: 1; transform: rotate(-3.5deg); transform-origin: left bottom; white-space: nowrap; }
  .subline { position: absolute; left: 182px; top: 362px; font-family: "Kalam", cursive; font-weight: 700; color: var(--navy); font-size: 35px; line-height: 46px; transform: rotate(-4deg); transform-origin: left top; white-space: nowrap; }

  .product-photo { position: absolute; left: 768px; top: 36px; width: 432px; height: 340px; border-radius: 45% 10% 40% 50% / 35% 20% 65% 60%; background: linear-gradient(160deg, #c8102e 0%, #2a45b8 45%, #1b2f9a 100%); box-shadow: 10px 20px 30px rgba(0,0,0,0.2); }

  .price-list { position: absolute; left: 66px; top: 490px; list-style: none; color: var(--navy); font-size: 28px; }
  .price-list li { display: flex; align-items: center; height: 41px; }
  .price-list svg { width: 28px; height: 30px; margin-right: 14px; flex: none; }

  .contact { position: absolute; left: 820px; top: 520px; }
  .contact__lead { color: var(--navy); font-size: 25px; margin-bottom: 12px; }
  .contact__line { color: var(--red); font-weight: 700; font-size: 28px; line-height: 34px; }

  .sport-photo { position: absolute; top: 680px; width: 261px; height: 190px; box-shadow: 0 4px 10px rgba(0,0,0,0.35); }
  .sport-photo--football { left: 90px; background: linear-gradient(180deg, #4f6d36 0%, #6f9a3c 55%, #5c8a2e 100%); }
  .sport-photo--boxing { left: 379px; background: linear-gradient(180deg, #3b3a38 0%, #b27a3a 55%, #d9a24a 100%); }

  .maker { position: absolute; left: 836px; top: 828px; color: var(--grey); }
  .maker__name { display: flex; align-items: center; font-size: 36px; line-height: 1; }
  .maker__square { width: 26px; height: 26px; background: var(--grey); margin-right: 12px; }
  .maker__tagline { font-size: 17px; margin-top: 10px; }
</style>
</head>
<body>
<main class="postcard">
  <svg class="sweep" viewBox="0 0 1200 930" aria-hidden="true">
    <path d="M0 800 C 250 700, 520 700, 790 930 L 0 930 Z" fill="var(--navy)"/>
  </svg>

  <header class="membership">
    <div class="membership__mark"></div>
    <div class="membership__divider"></div>
    <div class="membership__text">
      <p class="membership__org">Dental Technicians Guild</p>
      <p class="membership__status">Registered Member</p>
    </div>
  </header>

  <div class="product-photo" role="img" aria-label="Custom mouthguard in Union Jack colours"></div>

  <h1 class="headline">Guard your mouth</h1>
  <p class="subline">with custom made mouthguards<br>for sportsmen and women.</p>

  <ul class="price-list">
    <li><svg viewBox="0 0 28 30"><path d="M2 17 L10 27 L26 2" fill="none" stroke="var(--red)" stroke-width="3"/></svg>Custom made sports guards from £20 (Boxed)</li>
    <li><svg viewBox="0 0 28 30"><path d="M2 17 L10 27 L26 2" fill="none" stroke="var(--red)" stroke-width="3"/></svg>Bleaching trays from £28 (pair) (Boxed)</li>
    <li><svg viewBox="0 0 28 30"><path d="M2 17 L10 27 L26 2" fill="none" stroke="var(--red)" stroke-width="3"/></svg>Orthodontic retainers £28 (pair)</li>
  </ul>

  <section class="contact">
    <p class="contact__lead">For questions, please contact</p>
    <p class="contact__line">Tom or Gary (01872) 552317</p>
    <p class="contact__line">Harlow Dental Laboratory Ltd</p>
  </section>

  <div class="sport-photo sport-photo--football" role="img" aria-label="Football players contesting the ball on grass"></div>
  <div class="sport-photo sport-photo--boxing" role="img" aria-label="Boxing gloves on a gym floor beside a boxer's feet"></div>

  <footer class="maker">
    <p class="maker__name"><span class="maker__square"></span>Albion Dental Craft</p>
    <p class="maker__tagline">Carefully Fitted | Precisely Finished</p>
  </footer>
</main>
</body>
</html>
```